Psychotherapy Website - Based in London

I am a newly trained psychotherapist and need a new website for www.delphinecarrow.co.uk.

I offer therapy for addiction, relationships, trauma and many other issues people face in their lives.

I want the website to be welcoming, gentle, feminine and for people to feel safe.

I do not like a page site that scrolls through sections, rather each page should be separate. Here some examples that i like. Sectional rather than scrolled.

https://www.maribethvane.com/
https://www.thequietrooms.com/

The imagery should be around pink using the flower in the logo / wording and around the site:

Here is a link to the flower for ideas:
https://www.lookfindo.com/search?q=pink+gerbera

DelphineCarrow
Compassionate Psychotherapy

Is the logo and subheader for the website. Please use a typeface for the name that is appealing and professional.

Type face similar NOT EXLUSIVLY - JUST AN IDEA like this:
https://glowpostureclub.com/

Basic business card i created as a rough idea below.

I have also added the website copy.

The headers are

Homepage
About Me
Therapy
Common Questions
Blog
Contact Me

Target Market(s)

Clients who are dealing with stress, trauma, pain, addiction

Industry/Entity Type

Therapy and Psychology

Coding

Coded - Design and coding required

Number of Pages Required

5+ page

Font styles to use
Serif
Sans Serif
Script

Colors
0054AA
0677BA
7BADD7
CADEEF
E8F1F8
0094D4
00A9DD
6FCCEA
C7EBF8
E9F6FB
E54698
E96AAD
F1A4CE
F9D9EA
FCEFF6

Requirements
Must have
• Pink Gerbera Flower integrated into design
Nice to have
• Images but not to stock imagery. Needs to look authentic and natural
Should not have
• Stock images of people. Images are important but needs to feel REAL

```html
<!DOCTYPE html>
<html lang="en">
<head>
<meta charset="utf-8">
<title>DelphineCarrow · Compassionate Psychotherapy</title>
<link rel="stylesheet" href="https://fonts.googleapis.com/css2?family=Josefin+Sans:ital,wght@0,300;0,400;0,600;1,300&family=Montserrat:wght@500;600;700&family=Playfair+Display:wght@700&display=swap">
<style>
:root{
  --ink:#2e2e2e;
  --body:#555;
  --blue:#0054AA;
  --pink:#E54698;
  --pink-soft:#E96AAD;
  --plum-dark:#2a1330;
  --plum:#5b3a6c;
  --footer:#232323;
  --white:#fff;
  --star:#f5d90a;
}
*{margin:0;padding:0;box-sizing:border-box}
html,body{width:1200px;height:3411px;overflow:hidden}
body{position:relative;background:var(--white);font-family:"Josefin Sans",sans-serif;color:var(--body)}
.abs{position:absolute}

/* hero */
.hero{position:absolute;left:0;top:0;width:1200px;height:770px;overflow:hidden;
  background:radial-gradient(ellipse at 42% 45%,#6d5a85 0%,#4a3358 35%,var(--plum-dark) 80%)}
.hero-flower{position:absolute;left:520px;top:0;width:680px;height:740px;
  background:radial-gradient(ellipse at 70% 25%,#f45ec0 0%,#d62d98 35%,#a0166f 60%,rgba(90,30,80,0) 85%)}
.brand{position:absolute;display:flex;align-items:center;gap:10px}
.brand-dot{width:50px;height:50px;border-radius:50%;background:var(--pink)}
.brand-name{font-family:"Playfair Display",serif;font-weight:700;color:var(--white);font-size:28px;letter-spacing:1px;line-height:1}
.brand-tag{font-family:"Josefin Sans",sans-serif;color:var(--white);font-size:15px;margin-top:5px}
.nav{position:absolute;top:55px;left:495px;display:flex;gap:19px;font-family:"Montserrat",sans-serif;font-weight:600;font-size:14px;color:var(--white)}
.nav .active{color:var(--pink-soft)}
.hero-kicker{position:absolute;left:112px;top:205px;font-family:"Montserrat",sans-serif;font-weight:500;font-size:37px;color:var(--white)}
.hero-title{position:absolute;left:112px;top:253px;font-family:"Montserrat",sans-serif;font-weight:700;font-size:51px;color:var(--white)}
.hero-text{position:absolute;left:113px;top:340px;width:440px;font-size:21px;line-height:29px;color:var(--white)}
.btn-ghost{position:absolute;left:111px;top:458px;width:335px;height:63px;border:1.5px solid var(--white);border-radius:32px;
  font-family:"Montserrat",sans-serif;font-weight:500;font-size:18px;color:var(--white);display:flex;align-items:center;justify-content:center}
.dots{position:absolute;left:578px;top:587px;display:flex;gap:4px}
.dots span{width:12px;height:12px;border-radius:50%;border:1.5px solid var(--white)}
.dots span:first-child{background:var(--white)}
.wave{position:absolute;left:0}

/* welcome */
.portrait{position:absolute;left:99px;top:826px;width:403px;height:403px;border-radius:50%;
  background:radial-gradient(circle at 50% 40%,#f2d6c6 0%,#e9c9a3 25%,#e6f0f8 60%,#e8f1f8 100%)}
.eyebrow{font-family:"Montserrat",sans-serif;font-weight:600;font-size:23px;color:var(--blue)}
.welcome-eyebrow{position:absolute;left:569px;top:822px}
.welcome-title{position:absolute;left:569px;top:865px;width:540px;font-family:"Montserrat",sans-serif;font-weight:600;font-size:34px;line-height:40px;color:var(--ink)}
.welcome-copy{position:absolute;left:573px;top:1060px;width:525px;font-weight:300;font-size:17px;line-height:26.5px;color:var(--body)}
.welcome-copy p{margin-bottom:26.5px}
.btn-pink{position:absolute;left:569px;top:1764px;width:433px;height:60px;border-radius:30px;background:var(--pink);
  color:var(--white);font-family:"Montserrat",sans-serif;font-weight:500;font-size:17px;display:flex;align-items:center;justify-content:center}

/* testimonials */
.reviews{position:absolute;left:0;top:1918px;width:1200px;height:360px;background:var(--blue)}
.center{position:absolute;left:0;width:1200px;text-align:center}
.section-title{font-family:"Montserrat",sans-serif;font-weight:600;font-size:33px}
.review{position:absolute;top:2120px;width:300px;color:var(--white)}
.stars{color:var(--star);font-size:19px;letter-spacing:3px}
.quote{margin-top:12px;font-style:italic;font-weight:300;font-size:17px;line-height:26.5px}
.reviewer{margin-top:16px;font-weight:600;font-size:19px}
.chev{position:absolute;top:2200px;width:14px;height:24px}

/* newsletter */
.mist{position:absolute;left:0;top:2440px;width:1200px;height:660px;
  background:linear-gradient(180deg,#fff 0%,#f7f7f8 30%,#e2e3e7 55%,#c9cbd2 75%,#d8d9de 100%)}
.email-field{position:absolute;left:254px;top:2714px;width:692px;height:48px;border-bottom:1.5px solid #a9a9b0}
.email-field span{position:absolute;left:14px;top:16px;font-size:15px;color:#888}

/* footer */
.footer-bg{position:absolute;left:0;top:2830px;width:1200px;height:581px}
.foot-head{position:absolute;top:3036px;font-family:"Montserrat",sans-serif;font-weight:600;font-size:18px;color:var(--white)}
.foot-links{position:absolute;left:547px;top:3088px;list-style:none;font-size:16px;line-height:28.5px;color:var(--white)}
.contact{position:absolute;left:804px;color:var(--white);font-size:16px;line-height:19px;display:flex;gap:12px}
.contact svg{flex:none;margin-top:1px}
.divider{position:absolute;left:111px;top:3325px;width:978px;height:1px;background:#4a4a4a}
.copyright{position:absolute;left:111px;top:3360px;font-size:16px;color:var(--white)}
.social{position:absolute;top:3347px;width:42px;height:42px;border-radius:50%;border:1.5px solid var(--white)}
</style>
</head>
<body>

<header class="hero">
  <div class="hero-flower" role="img" aria-label="Close-up photograph of a pink gerbera flower"></div>
  <div class="brand" style="left:111px;top:45px">
    <div class="brand-dot"></div>
    <div>
      <div class="brand-name">DELPHINECARROW</div>
      <div class="brand-tag">Compassionate Psychotherapy</div>
    </div>
  </div>
  <nav class="nav">
    <span class="active">HOME</span><span>ABOUT ME</span><span>THERAPY</span><span>COMMON QUESTIONS</span><span>BLOG</span><span>CONTACT ME</span>
  </nav>
  <div class="hero-kicker">COMPASSIONATE</div>
  <div class="hero-title">PSYCHOTHERAPY</div>
  <p class="hero-text">I offer therapy for addiction, relationships, trauma and many other issues people face in their lives.</p>
  <div class="btn-ghost">SCHEDULE A CONSULTATION</div>
  <div class="dots"><span></span><span></span><span></span></div>
</header>

<svg class="wave" style="top:520px" width="1200" height="260" viewBox="0 0 1200 260">
  <defs>
    <linearGradient id="arc" x1="0" x2="1">
      <stop offset="0" stop-color="#0054AA"/><stop offset=".5" stop-color="#6a4aa8"/><stop offset="1" stop-color="#E54698"/>
    </linearGradient>
  </defs>
  <path d="M0 30 C160 160 300 220 420 210 C600 200 650 105 800 108 C960 112 1060 200 1200 200 L1200 260 L0 260 Z" fill="#fff"/>
  <path d="M0 20 C130 150 280 240 420 232 C600 222 660 120 810 118 C960 118 1070 215 1200 232" fill="none" stroke="url(#arc)" stroke-width="6"/>
</svg>

<main>
  <div class="portrait" role="img" aria-label="Portrait photograph of the therapist"></div>
  <div class="eyebrow welcome-eyebrow">Welcome</div>
  <h1 class="welcome-title">HOW DO WE RECOVER FROM ADDICTION, RELATIONSHIPS, TRAUMA AND MANY OTHER ISSUES</h1>
  <div class="welcome-copy">
    <p>Taking the first steps towards engaging in therapy can be a very personal journey.</p>
    <p>Whilst, it can be challenging, I will ensure to make this journey as safe and as comfortable for you as possible.</p>
    <p>Psychotherapy can help you see your current situation in new light, depth and clarity. It can change old and unhelpful perspectives and feelings about yourself and your life, and ultimately help you make positive changes. It might be the most important journey you'll ever make.</p>
    <p>I provide a and non-judgmental space where any issues can be explored in complete confidentiality.</p>
    <p>My practice is based in Richmond, where the room is homely, comfortable and welcoming. I believe a good environment contributes to great therapy.</p>
    <p>Alternately, I am also available to provide therapy online, if this environment is more accommodating for my clients.</p>
    <p>I am passionate about improving mental health and committed to offering therapy to all individuals regardless of their age, race, culture, disability, sexual orientation, or socio-economic background.</p>
  </div>
  <div class="btn-pink">CONTACT US FOR AN INITIAL CONSULTATION</div>

  <section class="reviews"></section>
  <svg class="wave" style="top:2270px" width="1200" height="200" viewBox="0 0 1200 200">
    <path d="M0 0 L1200 0 L1200 110 C1100 60 1000 70 900 80 C760 95 700 190 520 188 C300 186 150 100 0 8 Z" fill="#0054AA"/>
  </svg>
  <div class="center eyebrow" style="top:1988px;color:#fff">Reviews</div>
  <h2 class="center section-title" style="top:2030px;color:#fff">CLIENT TESTIMONIALS</h2>
  <div class="review" style="left:111px"><div class="stars">★★★★★</div><p class="quote">"Nemo enim ipsam voluptatem quia ol uptas sit aspernatur aut odit aut fugit, sed quia consequuntur magni dolores eos qui ratione volupta"</p><div class="reviewer">- Lara</div></div>
  <div class="review" style="left:453px"><div class="stars">★★★★★</div><p class="quote">"Nemo enim ipsam voluptatem quia ol uptas sit aspernatur aut odit aut fugit, sed quia consequuntur magni dolores eos qui ratione volupta"</p><div class="reviewer">- John</div></div>
  <div class="review" style="left:796px"><div class="stars">★★★★★</div><p class="quote">"Nemo enim ipsam voluptatem quia ol uptas sit aspernatur aut odit aut fugit, sed quia consequuntur magni dolores eos qui ratione volupta"</p><div class="reviewer">- Dazzy</div></div>
  <svg class="chev" style="left:50px" viewBox="0 0 14 24"><path d="M12 2 L2 12 L12 22" fill="none" stroke="#fff" stroke-width="3"/></svg>
  <svg class="chev" style="left:1134px" viewBox="0 0 14 24"><path d="M2 2 L12 12 L2 22" fill="none" stroke="#fff" stroke-width="3"/></svg>

  <div class="mist" role="img" aria-label="Soft misty mountain landscape"></div>
  <div class="center eyebrow" style="top:2531px">Receive updates</div>
  <h2 class="center section-title" style="top:2574px;color:var(--ink)">NEWSLETTER SUBSCRIPTION</h2>
  <p class="center" style="top:2636px;font-weight:300;font-size:20px;color:#666">Enter your email address to get updates</p>
  <div class="email-field">
    <span>✉ Email Address</span>
    <svg class="abs" style="right:10px;top:16px" width="26" height="12" viewBox="0 0 26 12"><path d="M0 6 H22 M17 1 L23 6 L17 11" fill="none" stroke="#E54698" stroke-width="2.5"/></svg>
  </div>
</main>

<footer>
  <svg class="footer-bg" width="1200" height="581" viewBox="0 0 1200 581">
    <defs>
      <linearGradient id="arc2" x1="0" x2="1">
        <stop offset="0" stop-color="#0054AA"/><stop offset=".5" stop-color="#6a4aa8"/><stop offset="1" stop-color="#E54698"/>
      </linearGradient>
    </defs>
    <path d="M0 236 C120 110 260 20 440 22 C620 24 680 160 800 160 C960 160 1060 60 1200 30 L1200 581 L0 581 Z" fill="#232323"/>
    <path d="M0 236 C120 96 260 2 440 4 C620 6 680 144 800 144 C960 144 1060 40 1200 14" fill="none" stroke="url(#arc2)" stroke-width="5"/>
  </svg>
  <div class="brand" style="left:111px;top:3082px">
    <div class="brand-dot" style="width:58px;height:58px"></div>
    <div>
      <div class="brand-name" style="font-size:30px">DELPHINECARROW</div>
      <div class="brand-tag" style="font-size:16px">Compassionate Psychotherapy</div>
    </div>
  </div>
  <div class="foot-head" style="left:547px">Quick Links</div>
  <ul class="foot-links"><li>Home</li><li>About Me</li><li>Therapy</li><li>Common Questions</li><li>Blog</li><li>Contact Me</li></ul>
  <div class="foot-head" style="left:804px">Contact Us</div>
  <div class="contact" style="top:3090px">
    <svg width="12" height="16" viewBox="0 0 12 16"><path d="M6 0 A6 6 0 0 1 12 6 C12 10 6 16 6 16 C6 16 0 10 0 6 A6 6 0 0 1 6 0 Z" fill="#E54698"/><circle cx="6" cy="6" r="2.2" fill="#232323"/></svg>
    <div>42 Larkfield Road<br>Thornbury<br>Middlesex<br>TW9 4LP</div>
  </div>
  <div class="contact" style="top:3184px">
    <svg width="14" height="14" viewBox="0 0 14 14"><path d="M3 0 L5.5 3.5 L4 5.5 C5 7.5 6.5 9 8.5 10 L10.5 8.5 L14 11 L12 14 C6 13.5 0.5 8 0 2 Z" fill="#E54698"/></svg>
    <div>07700 900418</div>
  </div>
  <div class="contact" style="top:3224px">
    <svg width="16" height="12" viewBox="0 0 16 12"><rect width="16" height="12" rx="1" fill="#E54698"/><path d="M0 1 L8 7 L16 1" fill="none" stroke="#232323" stroke-width="1.4"/></svg>
    <div>dc@delphinecarrow.co.uk</div>
  </div>
  <div class="contact" style="top:3264px">
    <svg width="15" height="15" viewBox="0 0 16 16"><circle cx="8" cy="8" r="7.5" fill="#E54698"/><path d="M1 8 H15 M8 0.5 C4 4 4 12 8 15.5 M8 0.5 C12 4 12 12 8 15.5" fill="none" stroke="#232323" stroke-width="1"/></svg>
    <div>www.delphinecarrow.co.uk</div>
  </div>
  <div class="divider"></div>
  <div class="copyright">© 2021 DelphineCarrow. All rights reserved.</div>
  <div class="social" style="left:943px"></div>
  <div class="social" style="left:994px"></div>
  <div class="social" style="left:1044px"></div>
</footer>

</body>
</html>
```